Business Card Design - Pediatric Dentist

We need a business card for a new dental office. We are a pediatric dentist in Austin Tx. I would like a design that use bright green and if possible light blue.

Target Market(s)

Marketed to young moms

Industry/Entity Type

Dental

Contact Information for Business Card

Marcus Pell DDS
Bramblewood Family Dentistry
428 E. Marlowe Road. Austin TX 78690
(512) 555 0183.

In the back i would like to state "we take most insurances, Tova & Vitacover" & a map

Colors
add136
cadf82
85cae6

```html
<!DOCTYPE html>
<html lang="en">
<head>
<meta charset="utf-8">
<title>Bramblewood Family Dentistry – Business Card</title>
<link rel="stylesheet" href="https://fonts.googleapis.com/css2?family=Marcellus+SC&family=Open+Sans:wght@300;400&family=Tinos:wght@400;700&display=swap">
<style>
  :root {
    --backdrop: #e9e9e6;
    --card-front: #eef6ea;
    --card-back: #eaf4fb;
    --green: #5db344;
    --green-bright: #add136;
    --green-soft: #cadf82;
    --blue: #4fa9e2;
    --blue-light: #85cae6;
    --ink: #1d1d1d;
    --map-light: #e4e6e8;
    --map-dark: #c9cdd1;
  }
  * { box-sizing: border-box; margin: 0; padding: 0; }
  html, body {
    width: 1200px; height: 873px; overflow: hidden;
    background: var(--backdrop);
  }
  .sheet {
    position: relative; width: 1200px; height: 873px;
    display: flex; align-items: center; justify-content: center; gap: 60px;
  }
  .card {
    position: relative; width: 520px; height: 297px;
    box-shadow: 0 2px 6px rgba(0,0,0,.18);
    overflow: hidden;
  }

  /* Front */
  .card--front { background: var(--card-front); }
  .mascot {
    position: absolute; left: 22px; top: 18px; width: 160px; height: 150px;
    background: radial-gradient(circle at 50% 45%, #ffffff 0 30%, var(--green-soft) 55%, var(--green) 100%);
    border-radius: 6px;
  }
  .practice-name {
    position: absolute; left: 200px; right: 20px; top: 38px;
    text-align: right; white-space: nowrap;
    font-family: "Marcellus SC", serif; font-size: 18px; color: var(--green);
    letter-spacing: .3px;
  }
  .dentist {
    position: absolute; left: 200px; right: 20px; top: 100px; text-align: center;
    font-family: "Open Sans", sans-serif; font-weight: 300; color: var(--blue);
  }
  .dentist__name { font-size: 44px; line-height: 1.1; white-space: nowrap; }
  .dentist__title { font-size: 22px; margin-top: 2px; }
  .contact {
    position: absolute; bottom: 16px;
    font-family: "Open Sans", sans-serif; font-size: 10px; color: var(--green);
    white-space: nowrap;
  }
  .contact--address { left: 22px; }
  .contact--phone { right: 22px; }

  /* Back */
  .card--back { background: var(--card-back); }
  .brand {
    position: absolute; left: 24px; top: 18px;
    display: flex; align-items: center; gap: 12px;
  }
  .brand__dot { width: 38px; height: 38px; border-radius: 50%; background: var(--green); flex: none; }
  .brand__name {
    font-family: "Tinos", serif; font-size: 22px; line-height: 1.05; color: var(--ink);
  }
  .insurance {
    position: absolute; left: 24px; top: 80px;
    font-family: "Tinos", serif; font-weight: 700; font-size: 15px; color: var(--ink);
    text-decoration: underline; line-height: 1.35;
  }
  .located {
    position: absolute; left: 24px; top: 128px;
    font-family: "Tinos", serif; font-weight: 700; font-size: 14px; color: var(--ink);
  }
  .map {
    position: absolute; right: 14px; bottom: 14px; width: 300px; height: 160px;
    background: linear-gradient(135deg, var(--map-light), var(--map-dark));
  }
  .pointer { position: absolute; left: 0; top: 0; }
</style>
</head>
<body>
<main class="sheet">

  <section class="card card--front" aria-label="Card front">
    <div class="mascot" role="img" aria-label="Cartoon tooth mascot illustration on a green star"></div>
    <p class="practice-name">Bramblewood Family Dentistry</p>
    <div class="dentist">
      <p class="dentist__name">Marcus Pell</p>
      <p class="dentist__title">DDS</p>
    </div>
    <p class="contact contact--address">Address: 428 E. Marlowe Road, Austin TX, 78690</p>
    <p class="contact contact--phone">Phone: (512) 555 0183</p>
  </section>

  <section class="card card--back" aria-label="Card back">
    <div class="brand">
      <span class="brand__dot"></span>
      <p class="brand__name">Bramblewood<br>Family Dentistry</p>
    </div>
    <p class="insurance">We take most insurances,<br>Tova &amp; Vitacover.</p>
    <p class="located">We are located here</p>
    <div class="map" role="img" aria-label="Street map showing the office location"></div>
    <svg class="pointer" width="520" height="297" viewBox="0 0 520 297" aria-hidden="true">
      <path d="M170 140 C 240 150, 270 200, 330 205" fill="none" stroke="var(--green)" stroke-width="2"/>
      <path d="M322 199 L332 205 L322 211" fill="none" stroke="var(--green)" stroke-width="2"/>
      <circle cx="344" cy="205" r="6" fill="var(--green)"/>
    </svg>
  </section>

</main>
</body>
</html>
```